A new medical waste company needs an attractive and modern flyer.

We are a new medical waste company disposing of biohazards waste, red bag waste and sharps disposal with a focus on customer service.

Background Information

Company Name
Korvane Waste

Industry
Medical waste management

Description of the organization and its target audience

We are a new medical waste company disposing of biohazardous waste, red bag waste and medical sharps.

Description

MODERN & ELEGANT HALF PAGE FLYER

Half page mailer (front and back) with a large image related to the medical field.

The Korvane Waste logo, with the company tag line “compliant waste solutions” should also be on front of the mailer.

Website (korvanewaste.example) & email (info@korvanewsate.example) on both sides of the flyer

Main headline
-Now you have options for your medical waste disposal

Who we serve
- Dentist
- Physicians
-Blood banks
-Tattoo parlors
-Assisted living facilities
-Laboratories
-Veterinarians

What we offer
-Straight forward pricing
-No hidden fees
-No long term contracts
-Free containers and red bags
-Routine scheduled pickups

Price $35.95
Updates

Remember this is a half page flyer. Please remove pricing from all future work.

Target Market(s)

- Dentist
- Physicians
-Blood banks
-Tattoo parlors
-Laboratories
-Veterinarians

Industry/Entity Type

It Company

Colors
33b8a4

Requirements
Must have
• See my website www.korvanewaste.example

```html
<!DOCTYPE html>
<html lang="en">
<head>
<meta charset="utf-8">
<title>Korvane Waste – Compliant Waste Solutions</title>
<link rel="stylesheet" href="https://fonts.googleapis.com/css2?family=Roboto+Condensed:wght@300;400;700&family=Lato:wght@400;700&display=swap">
<style>
  :root {
    --teal: #33b8a4;
    --ink: #231f20;
    --charcoal: #2b2727;
    --paper: #ffffff;
    --backdrop: #ecebea;
    --text: #1d1d1d;
  }
  * { margin: 0; padding: 0; box-sizing: border-box; }
  html, body { width: 907px; height: 1200px; overflow: hidden; }
  body { background: var(--backdrop); position: relative; font-family: "Lato", sans-serif; color: var(--text); }

  .flyer { position: absolute; left: 70px; top: 70px; width: 765px; height: 1065px; background: var(--paper); overflow: hidden; box-shadow: 0 2px 10px rgba(0,0,0,.15); }
  .flyer-shapes { position: absolute; inset: 0; }

  .brand { position: absolute; left: 44px; top: 42px; display: flex; align-items: center; gap: 14px; color: var(--paper); font-family: "Roboto Condensed", sans-serif; font-weight: 400; }
  .brand-dot { width: 40px; height: 40px; border-radius: 50%; background: var(--paper); opacity: .95; }
  .brand-name { font-size: 30px; letter-spacing: 2px; line-height: 1; padding-left: 14px; border-left: 1px solid rgba(255,255,255,.8); }
  .brand-name span { display: block; font-size: 17px; letter-spacing: 9px; margin-top: 6px; }

  .tagline { position: absolute; left: 46px; top: 230px; font-family: "Roboto Condensed", sans-serif; line-height: 1; white-space: nowrap; }
  .tagline .t1 { display: block; color: var(--teal); font-weight: 700; font-size: 68px; letter-spacing: -1px; transform: scaleX(.72); transform-origin: left center; }
  .tagline .t2 { display: block; color: var(--ink); font-weight: 400; font-size: 72px; margin-top: -6px; }
  .tagline .t3 { display: block; color: var(--ink); font-weight: 300; font-size: 50px; margin-top: 0; }

  .price-box { position: absolute; left: 442px; top: 466px; width: 286px; text-align: center; color: var(--paper); font-family: "Roboto Condensed", sans-serif; }
  .price-label { font-size: 68px; font-weight: 700; line-height: 1; }
  .price-value { font-family: "Lato", sans-serif; font-size: 40px; font-weight: 700; color: var(--teal); letter-spacing: 2px; margin-top: 8px; }

  .headline { position: absolute; left: 30px; top: 534px; font-family: "Roboto Condensed", sans-serif; }
  .headline h1 { color: var(--teal); font-size: 31px; font-weight: 700; letter-spacing: .5px; }
  .headline p { font-family: "Roboto Condensed", sans-serif; font-size: 23px; margin-top: 4px; color: var(--text); }

  .section-label { position: absolute; left: 0; height: 32px; padding: 0 0 0 38px; background: var(--teal); color: var(--paper); font-family: "Roboto Condensed", sans-serif; font-weight: 700; font-size: 26px; line-height: 32px; border-radius: 0 16px 16px 0; white-space: nowrap; }
  .label-serve { top: 617px; width: 208px; }
  .label-offer { top: 779px; width: 220px; }

  .list { position: absolute; list-style: none; font-size: 17px; line-height: 28px; white-space: nowrap; z-index: 2; }
  .list li { position: relative; padding-left: 16px; }
  .list li::before { content: ""; position: absolute; left: 0; top: 10px; width: 9px; height: 9px; border-radius: 50%; background: var(--teal); }
  .serve-a { left: 40px; top: 657px; }
  .serve-b { left: 258px; top: 655px; }
  .offer-a { left: 44px; top: 818px; line-height: 22px; }
  .offer-a li { margin-bottom: 6px; }
  .offer-a li::before { top: 8px; }
  .offer-b { left: 260px; top: 818px; line-height: 22px; }
  .offer-b li { margin-bottom: 6px; }
  .offer-b li::before { top: 8px; }

  .doctor-photo { position: absolute; left: 500px; top: 632px; width: 160px; height: 408px; border-radius: 70px 70px 8px 8px; background: linear-gradient(180deg, #f4f6f7 0%, #e3e9ec 55%, #cdbfa6 80%, #8a6a4c 100%); }

  .contact { position: absolute; left: 40px; top: 993px; color: var(--paper); font-size: 17px; line-height: 25px; }
  .contact div { display: flex; align-items: center; gap: 12px; }
  .contact svg { width: 18px; height: 18px; flex: none; }
</style>
</head>
<body>
  <main class="flyer">
    <svg class="flyer-shapes" viewBox="0 0 765 1065" aria-hidden="true">
      <defs>
        <linearGradient id="surgery" x1="0" y1="0" x2="1" y2="1">
          <stop offset="0" stop-color="#e9eef0"/>
          <stop offset=".45" stop-color="#a9c9d8"/>
          <stop offset="1" stop-color="#4fb0ad"/>
        </linearGradient>
        <linearGradient id="fadeLeft" x1="0" x2="1">
          <stop offset="0" stop-color="#fff" stop-opacity="1"/>
          <stop offset="1" stop-color="#fff" stop-opacity="0"/>
        </linearGradient>
      </defs>
      <path d="M0 0 H765 V8 C600 30 420 128 0 140 Z" fill="var(--teal)"/>
      <path d="M520 0 H765 V20 C700 22 640 30 585 45 C610 25 560 10 520 0 Z" fill="var(--ink)"/>
      <path d="M275 32 C420 20 600 12 765 18 V330 C600 420 450 468 275 482 Z" fill="url(#surgery)" role="img" aria-label="Photograph of a surgical team in scrubs operating in a theatre"/>
      <rect x="275" y="30" width="90" height="460" fill="url(#fadeLeft)"/>
      <path d="M0 470 C250 492 550 430 765 320 V350 C550 455 260 512 0 508 Z" fill="var(--teal)"/>
      <path d="M442 360 H728 V600 Q728 625 703 625 H467 Q442 625 442 600 Z" fill="var(--charcoal)"/>
      <path d="M0 935 C250 975 520 975 765 905 V1065 H0 Z" fill="var(--charcoal)"/>
      <path d="M460 980 C610 965 700 930 765 880 V835 C700 895 600 950 460 980 Z" fill="var(--teal)"/>
    </svg>

    <div class="brand">
      <div class="brand-dot"></div>
      <div class="brand-name">KORVANE<span>WASTE</span></div>
    </div>

    <h2 class="tagline"><span class="t1">COMPLIANT</span><span class="t2">WASTE</span><span class="t3">SOLUTIONS</span></h2>

    <div class="price-box">
      <div class="price-label">Price</div>
      <div class="price-value">$35.95</div>
    </div>

    <div class="headline">
      <h1>NOW YOU HAVE OPTIONS</h1>
      <p>for your medical waste disposal</p>
    </div>

    <div class="doctor-photo" role="img" aria-label="Photograph of a senior doctor in a white coat gesturing toward the text"></div>

    <div class="section-label label-serve">Who we serve</div>
    <ul class="list serve-a">
      <li>Dentist</li>
      <li>Physicians</li>
      <li>Blood banks</li>
      <li>Tattoo parlors</li>
    </ul>
    <ul class="list serve-b">
      <li>Assisted living<br>facilities</li>
      <li>Laboratories</li>
      <li>Veterinarians</li>
    </ul>

    <div class="section-label label-offer">Who we serve</div>
    <ul class="list offer-a">
      <li>Straight forward<br>pricing</li>
      <li>No hidden fees</li>
      <li>No long term contracts</li>
    </ul>
    <ul class="list offer-b">
      <li>Free containers<br>and red bags</li>
      <li>Routine scheduled pickups</li>
    </ul>

    <div class="contact">
      <div>
        <svg viewBox="0 0 20 20"><circle cx="10" cy="10" r="8.5" fill="none" stroke="var(--teal)" stroke-width="2"/><path d="M1.5 10 H18.5 M10 1.5 C5 6 5 14 10 18.5 M10 1.5 C15 6 15 14 10 18.5" fill="none" stroke="var(--teal)" stroke-width="1.6"/></svg>
        <span>www.korvanewaste.example</span>
      </div>
      <div>
        <svg viewBox="0 0 20 20"><rect x="1" y="4" width="18" height="12" rx="1" fill="var(--teal)"/><path d="M1.5 4.5 L10 11 L18.5 4.5" fill="none" stroke="var(--charcoal)" stroke-width="1.6"/></svg>
        <span>info@korvanewsate.example</span>
      </div>
    </div>
  </main>
</body>
</html>
```